Website Design for Business Law Firm

We have a logo and now we would like a web site design for our new website. Our small firm provides creative and aggressive transactional (not litigation) legal services to advise healthcare, technology, internet-based and traditional companies and investors in such companies on healthcare, technology, financing, mergers/acquisitions, real estate and other transactions, legal compliance and general corporate and business matters.

We would like to see a website design that is professional and appropriate for executives, professionals, investors and government regulators to visit, that conveys professionalism and competence while being a little edgy and modern - no typical legal motifs such as gavels, books, or scales of justice. We advise businesses and investors and guide them through complicated issues quickly, capably and differently from other law firms. We are part of the business team and get things done.

The logo is attached, and we like gray as a color to complement it. The intention of the logo is to convey that in a storm or challenging time, people come to this firm, and people come to this firm when they need the power and disruption to change things or shake them up.

I have also enclosed a picture of our business card for consideration.

On the other hand, you can check out the current simple site at www.quenlow.example to see we have used a space motif in the past to evoke that we help create stars (the nebula featured there). This is not a necessary part of the new website and it may look better without it.

We appreciate your creativity and look forward to designs.

Industry/Entity Type

Business

Requirements
Must have
• We anticipate the following pages, and you may submit different ideas for the different pages:
• 1. Landing page
• 2. Services pages - healthcare, IT/Technology, general counsel services, financings, mergers/acquisitions, mediation/arbitration, procurement and productization
• 3. About Us including contact information
• Our name and contact information:
• Quenlow Law Firm, P.C.
• 7816 SW 19th Ave.
• Portland, OR 97213
• phone: 555.614.2873
• fax: 555.730.4158
Nice to have
• Please consider designs that enhance the impressions we are looking for
Should not have
• Please no gavels, scales of justice, law books, or similar traditional legal imagery.

```html
<!DOCTYPE html>
<html lang="en">
<head>
<meta charset="utf-8">
<title>Quenlow Law Firm</title>
<link rel="stylesheet" href="https://fonts.googleapis.com/css2?family=Oswald:wght@300;400&family=Roboto:wght@400;500&display=swap">
<style>
:root{
  --space-deep:#05070c;
  --panel:#141414;
  --panel-dark:#111;
  --heading:#6f8b92;
  --heading-soft:#7f979c;
  --text:#b5b5b5;
  --text-dim:#9a9a9a;
  --white:#f1f1f1;
  --nav-top:#8b939b;
  --nav-bottom:#4c545c;
  --btn-top:#7a828a;
  --btn-bottom:#4a5158;
  --rule:#2c2c2c;
  --footer:#222;
}
*{margin:0;padding:0;box-sizing:border-box}
html,body{width:1003px;height:1200px;overflow:hidden;background:var(--space-deep)}
body{position:relative;font-family:Arial,Helvetica,sans-serif;color:var(--text)}
.space-bg{position:absolute;left:0;top:0;width:1003px;height:1200px;
  background:linear-gradient(180deg,#1a2032 0,#1e2233 35%,#121624 55%,#05070c 75%,#000 100%)}
.abs{position:absolute}
.header{left:143px;top:0;width:717px;height:152px;background:var(--panel-dark)}
.brand{left:158px;top:26px;width:216px;height:52px;display:flex;align-items:center;gap:10px}
.brand-mark{width:16px;height:16px;background:var(--heading)}
.brand-name{font-family:Oswald,sans-serif;font-weight:300;font-size:26px;letter-spacing:6px;color:var(--white)}
.contact{right:165px;top:29px;font-size:10px;color:var(--text-dim);line-height:21.5px}
.contact div{display:flex;align-items:center;gap:8px}
.nav{left:157px;top:94px;width:689px;height:45px;background:linear-gradient(var(--nav-top),var(--nav-bottom));display:flex;align-items:center;padding-left:28px;box-shadow:0 1px 2px #000}
.nav a{font-family:Oswald,sans-serif;font-weight:300;font-size:11.5px;color:var(--white);text-decoration:none;margin-right:47.5px}
.hero-title{left:0;width:1003px;top:214px;text-align:center;font-family:Oswald,sans-serif;font-size:54px;color:var(--heading);letter-spacing:1px;line-height:72px}
.hero-text{left:194px;width:615px;top:294px;text-align:center;font-family:Oswald,sans-serif;font-weight:400;font-size:13.5px;line-height:23.5px;color:var(--white);text-transform:uppercase}
.hero-btn{left:407px;top:386px;width:189px;height:42px;border-radius:3px;background:linear-gradient(var(--btn-top),var(--btn-bottom));color:var(--white);font-family:Roboto,sans-serif;font-size:14px;display:flex;align-items:center;justify-content:center}
.slide-arrow{top:305px;width:34px;height:34px;background:rgba(255,255,255,.1);display:flex;align-items:center;justify-content:center}
.main{left:143px;top:482px;width:717px;height:718px;background:var(--panel)}
.h2{font-family:Oswald,sans-serif;font-weight:400;font-size:18px;color:var(--heading);text-transform:uppercase}
.intro{left:158px;top:522px;width:670px;font-size:9.6px;line-height:18.5px}
.mini-arrows{left:817px;top:586px;display:flex;gap:2px}
.mini-arrows span,.tm-arrows span{width:11px;height:11px;background:#3b3b3b;display:flex;align-items:center;justify-content:center}
.photo{position:absolute}
.svc-title{font-family:Oswald,sans-serif;font-weight:300;font-size:11.5px;color:var(--heading-soft)}
.body-text{font-size:8.8px;line-height:14.4px;color:var(--text-dim)}
.rule{left:158px;top:827px;width:688px;height:1px;background:var(--rule)}
.btn{height:19px;padding:0 13px;border-radius:2px;background:linear-gradient(var(--btn-top),var(--btn-bottom));color:var(--white);font-size:8px;font-weight:bold;display:flex;align-items:center}
.blog-item{left:646px;width:210px;height:60px}
.blog-item .thumb{position:absolute;left:0;top:0;width:60px;height:55px}
.blog-item .txt{position:absolute;left:75px;top:0;width:135px}
.blog-item .body-text{font-size:8px}
.blog-title{font-size:8.8px;color:var(--heading-soft);line-height:14px}
.date{font-style:italic;font-size:8px;color:var(--heading);margin-top:3px}
.footer{left:158px;top:1134px;width:688px;height:55px;background:var(--footer)}
.footer-links{left:173px;top:1148px;font-size:8px;color:var(--text);word-spacing:1px}
.footer-links span{margin:0 9px}
.copyright{left:173px;top:1167px;font-size:8px;color:var(--text)}
.follow{left:698px;top:1152px;display:flex;align-items:center;gap:3px;font-size:6.5px;color:var(--text)}
.social{width:19px;height:19px;border-radius:50%}
</style>
</head>
<body>
<div class="space-bg" role="img" aria-label="Space nebula photograph background"></div>

<div class="abs header"></div>
<div class="abs brand"><span class="brand-mark"></span><span class="brand-name">QUENLOW</span></div>
<div class="abs contact">
  <div><svg width="10" height="11" viewBox="0 0 10 11"><rect x="2" y="0.5" width="6" height="10" rx="1" fill="none" stroke="#9a9a9a"/><rect x="4" y="8" width="2" height="1" fill="#9a9a9a"/></svg>Phone :555.730.4158</div>
  <div><svg width="11" height="8" viewBox="0 0 11 8"><rect width="11" height="8" fill="#9a9a9a"/><path d="M0 0L5.5 4.5 11 0" stroke="#111" fill="none"/></svg>Fax : 555.730.4158</div>
</div>
<nav class="abs nav">
  <a>HOME</a><a>ABOUT US</a><a>SERVICES</a><a>FAQ'S</a><a>APPOINTMENT</a><a>TESTIMONIALS</a><a>CONTACT US</a>
</nav>

<div class="abs slide-arrow" style="left:108px"><svg width="10" height="14"><path d="M8 1L2 7l6 6" stroke="#777" fill="none"/></svg></div>
<div class="abs slide-arrow" style="left:864px"><svg width="10" height="14"><path d="M2 1l6 6-6 6" stroke="#777" fill="none"/></svg></div>
<h1 class="abs hero-title">QUENLOW</h1>
<p class="abs hero-text">It is a law firm with services in companies on healthcare, technology, financing, mergers/acquisitions, real estate and other transactions, legal compliance and general corporate and business matters.</p>
<div class="abs hero-btn">Click here for more Info</div>

<div class="abs main"></div>
<h2 class="abs h2" style="left:158px;top:494px">Welcome to Quenlow Law</h2>
<p class="abs intro">It is a law firm with services in companies on healthcare, technology, financing, mergers/acquisitions, real estate and other transactions, legal compliance and general corporate and business matters.</p>

<h2 class="abs h2" style="left:158px;top:580px">Our Services</h2>
<div class="abs mini-arrows"><span><svg width="5" height="7"><path d="M4 1L1 3.5 4 6" stroke="#999" fill="none"/></svg></span><span><svg width="5" height="7"><path d="M1 1l3 2.5L1 6" stroke="#999" fill="none"/></svg></span></div>

<div class="photo" style="left:158px;top:616px;width:213px;height:100px;background:linear-gradient(135deg,#2c3f73,#4a63a0 60%,#26355f)" role="img" aria-label="Capitol dome and medical emblem in blue"></div>
<div class="photo" style="left:394px;top:616px;width:213px;height:100px;background:linear-gradient(135deg,#0f2f4c,#3a84b5 50%,#123450)" role="img" aria-label="Hand touching glowing digital tiles"></div>
<div class="photo" style="left:630px;top:616px;width:213px;height:100px;background:linear-gradient(135deg,#1d1a14,#b89a5a 45%,#e8e0cc)" role="img" aria-label="Calculator, pen and financial papers"></div>

<div class="abs svc-title" style="left:158px;top:726px">HEALTHCARE</div>
<div class="abs svc-title" style="left:394px;top:726px">TECHNOLOGY</div>
<div class="abs svc-title" style="left:630px;top:726px">FINANCING</div>
<p class="abs body-text" style="left:160px;top:749px;width:212px">It is a law firm with services in companies on health-care, technology, financing, mergers/acquisitions, real estate and other transactions, legal compliance and general corporate and business matters.</p>
<p class="abs body-text" style="left:396px;top:749px;width:212px">It is a law firm with services in companies on health-care, technology, financing, mergers/acquisitions, real estate and other transactions, legal compliance and general corporate and business matters.</p>
<p class="abs body-text" style="left:632px;top:749px;width:212px">It is a law firm with services in companies on health-care, technology, financing, mergers/acquisitions, real estate and other transactions, legal compliance and general corporate and business matters.</p>

<div class="abs rule"></div>

<h2 class="abs h2" style="left:160px;top:842px">About Us</h2>
<h2 class="abs h2" style="left:396px;top:842px">Testimonials</h2>
<h2 class="abs h2" style="left:646px;top:841px">Our Blog</h2>

<div class="photo" style="left:158px;top:874px;width:204px;height:112px;background:linear-gradient(120deg,#8ea3b8,#d9dde2 50%,#9c8b78)" role="img" aria-label="Business team meeting around a table"></div>
<p class="abs body-text" style="left:160px;top:994px;width:210px">It is a law firm with services in companies on health-care, technology, financing, mergers/acquisitions, real estate and other transactions, legal compliance and general corporate and business matters.estate and other transactions, legal compliance and general corporate and business matters.</p>
<div class="abs btn" style="left:161px;top:1090px">Read More</div>

<div class="photo" style="left:394px;top:874px;width:222px;height:105px;background:linear-gradient(120deg,#d8d2c6,#7fb3d8 55%,#5a4a3c)" role="img" aria-label="Portrait of a smiling client"></div>
<div class="abs svc-title" style="left:398px;top:990px">MARLON TEAGUE</div>
<div class="abs tm-arrows" style="left:593px;top:992px;display:flex;gap:2px"><span><svg width="5" height="7"><path d="M4 1L1 3.5 4 6" stroke="#999" fill="none"/></svg></span><span><svg width="5" height="7"><path d="M1 1l3 2.5L1 6" stroke="#999" fill="none"/></svg></span></div>
<div class="abs date" style="left:398px;top:1008px;margin:0">Posted on 23 october 2013</div>
<p class="abs body-text" style="left:398px;top:1027px;width:220px">It is a law firm with services in companies on healthcare, technology, financing, mergers/acquisitions, real estate and other transactions, legal compliance...</p>
<div class="abs btn" style="left:397px;top:1092px">View More</div>

<div class="abs blog-item" style="top:874px">
  <div class="thumb" style="background:linear-gradient(135deg,#e9e4de,#b08a6e)" role="img" aria-label="Blog author portrait"></div>
  <div class="txt"><div class="blog-title">It is a law firm with services</div><div class="body-text">It is a law firm with services in com-<br>panies on healthcare...</div><div class="date">Posted on 23 october 2013</div></div>
</div>
<div class="abs blog-item" style="top:944px">
  <div class="thumb" style="background:linear-gradient(135deg,#e6ded2,#9b7a5e)" role="img" aria-label="Family group photo"></div>
  <div class="txt"><div class="blog-title">It is a law firm with services</div><div class="body-text">It is a law firm with services in com-<br>panies on healthcare...</div><div class="date">Posted on 23 october 2013</div></div>
</div>
<div class="abs blog-item" style="top:1015px">
  <div class="thumb" style="background:linear-gradient(135deg,#efe9e2,#b5896a)" role="img" aria-label="Blog author portrait"></div>
  <div class="txt"><div class="blog-title">It is a law firm with services</div><div class="body-text">It is a law firm with services in com-<br>panies on healthcare...</div><div class="date">Posted on 23 october 2013</div></div>
</div>
<div class="abs btn" style="left:648px;top:1092px">View More</div>

<div class="abs footer"></div>
<div class="abs footer-links">Home<span>|</span>About Us<span>|</span>Services<span>|</span>Faq's<span>|</span>Appointment<span>|</span>Testimonials<span>|</span>Contact us</div>
<div class="abs copyright">Copyright © 2013. Quenlow. All Rights Reserved</div>
<div class="abs follow">FOLLOW US :
  <span class="social" style="background:#3b5fa8"></span>
  <span class="social" style="background:#3a9ad6"></span>
  <span class="social" style="background:#2a6f94"></span>
  <span class="social" style="background:#e69a1e"></span>
</div>
</body>
</html>
```